Webpage for balustrade importer and installer

We are a balustrade importer and installer. We sell a few different products mostly connected with glass and aluminum. We sell balconies, stairs, shower glass, mirrors, splash back glass, office partitions, glass dors and walls.

Coded - Design and coding required

```html
<!DOCTYPE html>
<html lang="en">
<head>
<meta charset="utf-8">
<title>KLARVIK – Balustrade Importer and Installer</title>
<link rel="stylesheet" href="https://fonts.googleapis.com/css2?family=Poppins:wght@300;400;500;600;700&family=Libre+Baskerville:wght@700&display=swap">
<style>
:root{
  --blue:#1a3d9c;
  --blue-dark:#13307f;
  --blue-mid:#1f6fbf;
  --yellow:#f9b700;
  --text:#555;
  --grey-bg:#f2f2f2;
  --white:#fff;
}
*{margin:0;padding:0;box-sizing:border-box}
html,body{width:1200px;height:3416px;overflow:hidden}
body{position:relative;font-family:'Poppins',sans-serif;color:var(--text);background:var(--white)}
.abs{position:absolute}
a{color:inherit;text-decoration:none}

/* top bar */
.topbar{left:0;top:0;width:1200px;height:32px;background:var(--blue);color:#fff;font-size:13px}
.topbar .call{left:139px;top:7px;display:flex;align-items:center;gap:8px}
.topbar .lang{left:872px;top:7px;display:flex;align-items:center;gap:8px}
.topbar .sep{left:955px;top:9px;width:1px;height:14px;background:rgba(255,255,255,.5)}
.topbar .dot{top:11px;width:10px;height:10px;border-radius:50%;background:#fff}

/* header */
.header{left:0;top:32px;width:1200px;height:102px;background:#fff}
.logo{font-family:'Poppins',sans-serif;font-weight:300;font-size:50px;letter-spacing:-1px;color:var(--blue);line-height:1}
.header .logo{left:139px;top:24px}
.nav{left:426px;top:45px;display:flex;gap:28px;font-size:13.5px;font-weight:500;color:#222}
.nav .active{color:var(--blue)}
.btn-yellow{background:var(--yellow);color:#fff;font-weight:500;display:flex;align-items:center;justify-content:center;border-radius:2px}
.header .btn-yellow{left:918px;top:34px;width:140px;height:36px;font-size:14px}

/* hero */
.hero{left:0;top:134px;width:1200px;height:556px;background:linear-gradient(180deg,#d8b48f 0%,#6c8b5d 18%,#4b6a4a 36%,#8a5a4a 55%,#6f4238 78%,#4b2a26 100%)}
.hero-title{left:0;top:160px;width:1200px;text-align:center;color:#fff;font-weight:700;font-size:46px;text-shadow:0 2px 6px rgba(0,0,0,.6)}
.hero-sub{left:0;top:224px;width:1200px;text-align:center;color:#fff;font-weight:600;font-size:24px;line-height:39px;text-shadow:0 2px 5px rgba(0,0,0,.6)}
.hero-btn{left:520px;top:340px;width:160px;height:44px;background:var(--blue);color:#fff;border:2px solid #fff;border-radius:3px;font-size:15px;font-weight:500;display:flex;align-items:center;justify-content:center}
.hero-edge{left:0;top:456px}

/* welcome */
.welcome h1{left:141px;top:752px;font-size:38px;font-weight:700;color:var(--blue)}
.welcome p{left:141px;top:828px;width:460px;font-size:15px;line-height:26.4px;text-align:justify;color:#666}
.welcome .btn-yellow{left:141px;top:1100px;width:143px;height:38px;font-size:15px}
.welcome .frame{left:696px;top:718px;width:362px;height:297px;background:var(--blue-mid)}
.welcome .photo{left:648px;top:730px;width:399px;height:408px;background:linear-gradient(160deg,#c9c5bd 0%,#8d7a68 45%,#5a4535 80%,#3d2e24 100%)}

/* featured */
.featured{left:0;top:1210px;width:1200px;height:543px;background:var(--grey-bg)}
.section-title{width:1200px;left:0;text-align:center;font-weight:700;color:var(--blue)}
.featured .section-title{top:1270px;font-size:35px}
.featured .intro{left:0;top:1322px;width:1200px;text-align:center;font-size:15px;line-height:27px;color:#666}
.card{top:1420px;width:218px}
.card .img{width:218px;height:212px}
.card .label{margin-top:4px;height:39px;background:var(--blue-mid);color:#fff;font-size:17px;font-weight:500;display:flex;align-items:center;justify-content:center}
.arrow{width:22px;height:36px}

/* services */
.services .section-title{top:1812px;font-size:30px}
.service{top:1892px;width:281px;height:126px;background:var(--grey-bg);border:1px solid #ddd;display:flex;align-items:center;padding-left:21px;gap:20px}
.service .icon{width:90px;height:90px;border-radius:50%;background:#fff;border:1px solid #ddd;flex:none;display:flex;align-items:center;justify-content:center}
.service .name{font-size:23px;line-height:32px;color:#222}

/* quote */
.quote{left:0;top:2092px;width:1200px;height:560px;background:linear-gradient(90deg,#3a2f25 0%,#6b5a43 20%,#504330 50%,#3b3024 75%,#2a221b 100%)}
.quote h2{left:0;top:2140px;width:1200px;text-align:center;font-family:'Libre Baskerville',serif;font-size:25px;color:#fff}
.quote .sub{left:0;top:2184px;width:1200px;text-align:center;font-size:16px;color:#fff;font-weight:500}
.field{background:#fff;border:1px solid #ddd;font-size:14.5px;color:#333;padding-left:18px;display:flex;align-items:center}
.field.msg{align-items:flex-start;padding-top:11px;padding-left:11px}
.quote .btn-yellow{left:521px;top:2543px;width:158px;height:44px;font-size:18px}

/* testimonials */
.testi .section-title{top:2708px;font-size:29px}
.avatar{left:555px;top:2779px;width:90px;height:90px;border-radius:50%;background:linear-gradient(180deg,#d9d9d9,#8e8e8e);border:3px solid #fff;box-shadow:0 0 0 1px #ccc}
.testi p{left:180px;top:2892px;width:840px;text-align:center;font-size:15px;line-height:26.5px;color:#666}
.testi .who{left:0;top:2986px;width:1180px;text-align:center;font-size:14.5px;color:var(--blue);font-weight:500}

/* footer */
.footer{left:0;top:3055px;width:1200px;height:317px;background:var(--blue)}
.footer .logo{left:139px;top:3105px;color:#fff;font-size:50px}
.footer .soc{top:3186px;width:32px;height:32px;border-radius:50%;background:var(--yellow)}
.f-title{top:3100px;font-size:19px;font-weight:600;color:#fff}
.f-rule{top:3140px;width:46px;height:2px;background:#fff}
.f-links{left:367px;top:3158px;font-size:14px;line-height:28px;color:#fff}
.f-news{left:563px;top:3157px;font-size:14px;line-height:25px;color:#fff}
.f-input{left:563px;top:3222px;width:195px;height:40px;background:#4e86c9;color:#fff;font-size:14px;padding-left:15px;display:flex;align-items:center}
.f-go{left:758px;top:3222px;width:38px;height:40px;background:var(--yellow);display:flex;align-items:center;justify-content:center}
.f-contact{left:900px;color:#fff;font-size:14px;line-height:28.5px}
.f-ico{left:860px;width:24px;height:24px;border-radius:50%;background:#4e86c9;display:flex;align-items:center;justify-content:center}
.copy{left:0;top:3372px;width:1200px;height:44px;background:var(--blue-dark);color:#fff;font-size:14.5px;display:flex;align-items:center;justify-content:center}
</style>
</head>
<body>

<!-- top bar -->
<div class="abs topbar">
  <div class="abs call">
    <svg width="16" height="16" viewBox="0 0 24 24"><path d="M6.6 10.8a15 15 0 0 0 6.6 6.6l2.2-2.2a1 1 0 0 1 1-.25 11.4 11.4 0 0 0 3.6.57 1 1 0 0 1 1 1V20a1 1 0 0 1-1 1A17 17 0 0 1 3 4a1 1 0 0 1 1-1h3.5a1 1 0 0 1 1 1c0 1.25.2 2.45.57 3.57a1 1 0 0 1-.25 1z" fill="none" stroke="#fff" stroke-width="1.8"/></svg>
    <span>Call Us: +123-5550142876</span>
  </div>
  <div class="abs lang">
    <svg width="20" height="20" viewBox="0 0 24 24" fill="none" stroke="#fff" stroke-width="1.4"><circle cx="12" cy="12" r="9"/><ellipse cx="12" cy="12" rx="4" ry="9"/><path d="M3 12h18M4.5 7.5h15M4.5 16.5h15"/></svg>
    <span>Import</span>
  </div>
  <div class="abs sep"></div>
  <div class="abs dot" style="left:980px"></div>
  <div class="abs dot" style="left:1013px"></div>
  <div class="abs dot" style="left:1047px"></div>
</div>

<!-- header -->
<header class="abs header">
  <div class="abs logo">KLARVIK</div>
  <nav class="abs nav">
    <a class="active">HOME</a><a>ABOUT US</a><a>PRODUCTS</a><a>SERVICES</a><a>CONTACT US</a>
  </nav>
  <a class="abs btn-yellow">INQUIRE NOW</a>
</header>

<!-- hero -->
<section class="abs hero" role="img" aria-label="Wooden deck terrace with glass balustrade overlooking a green coastline and the sea at sunset"></section>
<h1 class="abs hero-title">Balustrade Importer and Installer</h1>
<p class="abs hero-sub">We sell a few different products mostly connected<br>with glass and aluminum.</p>
<a class="abs hero-btn">LEARN MORE</a>
<svg class="abs hero-edge" width="1200" height="234" viewBox="0 0 1200 234">
  <polygon points="0,220 600,147 1200,220 1200,234 0,234" fill="#fff"/>
  <polyline points="0,220 600,147 1200,220" fill="none" stroke="#1f6fbf" stroke-width="5"/>
</svg>

<!-- welcome -->
<section class="welcome">
  <h1 class="abs">Welcome to KLARVIK</h1>
  <p class="abs">Lorem Ipsum is simply dummy text of the printing and typesetting industry. Lorem Ipsum has been the industry's standard dummy text ever since the 1500s, when an unknown printer took a galley of type and scrambled it to make a type specimen book. It has survived not only five centuries, but also the leap into electronic typesetting, remaining essentially unchanged. It was polarised in the 1960s with the release of Letraset sheets containg Lorem Ipsum passages, and more recently with desktop publishing software.</p>
  <a class="abs btn-yellow">LEARN MORE</a>
  <div class="abs frame"></div>
  <div class="abs photo" role="img" aria-label="Interior staircase with wooden steps and a frameless glass balustrade"></div>
</section>

<!-- featured products -->
<section class="abs featured"></section>
<h2 class="abs section-title" style="top:1270px;font-size:35px">Featured Products</h2>
<p class="abs" style="left:0;top:1322px;width:1200px;text-align:center;font-size:15px;line-height:27px;color:#666">We are a balustrade importer and installer. We sell a few different products mostly connected with glass and aluminum.<br>We sell balconies, stairs, shower glass, mirrors, splash back glass, office partitions, glass dors and walls.</p>
<svg class="abs arrow" style="left:78px;top:1522px" viewBox="0 0 22 36"><polyline points="18,3 4,18 18,33" fill="none" stroke="#777" stroke-width="3"/></svg>
<svg class="abs arrow" style="left:1097px;top:1522px" viewBox="0 0 22 36"><polyline points="4,3 18,18 4,33" fill="none" stroke="#777" stroke-width="3"/></svg>
<div class="abs card" style="left:141px"><div class="img" role="img" aria-label="Metal balcony railing beside bare winter trees" style="background:linear-gradient(180deg,#d9dde0,#8c8a85 60%,#5c5650)"></div><div class="label">Balconies</div></div>
<div class="abs card" style="left:373px"><div class="img" role="img" aria-label="Outdoor concrete stairs with steel railing against a grey wall" style="background:linear-gradient(180deg,#5d6670,#8a8f94 55%,#b8b4ad)"></div><div class="label">Stairs</div></div>
<div class="abs card" style="left:605px"><div class="img" role="img" aria-label="Bathroom with frosted glass shower screen" style="background:linear-gradient(90deg,#e8e4de,#d7dde0 50%,#c4b29a)"></div><div class="label">Shower Glass</div></div>
<div class="abs card" style="left:837px"><div class="img" role="img" aria-label="Glass sliding doors opening onto a garden" style="background:linear-gradient(180deg,#eef0ee,#cfd3cf 50%,#9aa88f)"></div><div class="label">Mirrors</div></div>

<!-- services -->
<h2 class="abs section-title" style="top:1812px;font-size:30px">Services Offered</h2>
<div class="abs service" style="left:141px">
  <div class="icon"><svg width="56" height="50" viewBox="0 0 56 50" fill="none" stroke="#f9b700" stroke-width="2"><path d="M4 14h48M4 44h48"/><path d="M8 14v30M16 14v30M24 14v30M32 14v30M40 14v30M48 14v30"/><path d="M28 2v8M24 6h8"/></svg></div>
  <div class="name">Import new<br>Varieties</div>
</div>
<div class="abs service" style="left:459px">
  <div class="icon"><svg width="50" height="54" viewBox="0 0 50 54" fill="none" stroke="#f9b700" stroke-width="2"><rect x="6" y="6" width="38" height="42"/><path d="M25 6v42M6 26h38M2 6h46M2 50h46"/></svg></div>
  <div class="name">Installation<br>Services</div>
</div>
<div class="abs service" style="left:776px">
  <div class="icon"><svg width="46" height="56" viewBox="0 0 46 56" fill="none" stroke="#f9b700" stroke-width="2"><path d="M15 4h16l-4 10H19z"/><path d="M19 14C6 22 4 34 4 40c0 8 6 12 19 12s19-4 19-12c0-6-2-18-15-26"/><circle cx="23" cy="36" r="10"/><path d="M26 31h-5a2.5 2.5 0 0 0 0 5h4a2.5 2.5 0 0 1 0 5h-5M23 28v16"/></svg></div>
  <div class="name">Affordable<br>Prices</div>
</div>

<!-- quote -->
<section class="abs quote" role="img" aria-label="Dimly lit lounge with a sofa, a potted plant and tall windows"></section>
<h2 class="abs" style="left:0;top:2140px;width:1200px;text-align:center;font-family:'Libre Baskerville',serif;font-size:25px;color:#fff">GET A QUOTE</h2>
<p class="abs" style="left:0;top:2184px;width:1200px;text-align:center;font-size:16px;color:#fff;font-weight:500">Fill all the details. Our experts will reach you soon.</p>
<div class="abs field" style="left:289px;top:2243px;width:305px;height:39px">First Name</div>
<div class="abs field" style="left:605px;top:2243px;width:305px;height:39px">Last Name</div>
<div class="abs field" style="left:289px;top:2295px;width:305px;height:39px">Email Address</div>
<div class="abs field" style="left:605px;top:2295px;width:305px;height:39px">Phone Number</div>
<div class="abs field" style="left:289px;top:2346px;width:621px;height:38px">Select Product</div>
<div class="abs field msg" style="left:289px;top:2396px;width:621px;height:111px">Message ( Optional )</div>
<a class="abs btn-yellow" style="left:521px;top:2543px;width:158px;height:44px;font-size:18px">INQUIRE NOW</a>

<!-- testimonials -->
<h2 class="abs section-title" style="top:2708px;font-size:29px">Testimonials</h2>
<div class="abs avatar" role="img" aria-label="Portrait photo of the customer"></div>
<svg class="abs arrow" style="left:78px;top:2865px" viewBox="0 0 22 36"><polyline points="18,3 4,18 18,33" fill="none" stroke="#777" stroke-width="3"/></svg>
<svg class="abs arrow" style="left:1097px;top:2865px" viewBox="0 0 22 36"><polyline points="4,3 18,18 4,33" fill="none" stroke="#777" stroke-width="3"/></svg>
<p class="abs" style="left:180px;top:2892px;width:840px;text-align:center;font-size:15px;line-height:26.5px;color:#666">Lorem Ipsum is simply dummy text of the printing and typese tting industry. Lorem Ipsum has been the industry's standard dummy text ever since the 1500s, when an unknown printer took a galley of type and scrambled it to make a type specimen book. It has survived</p>
<div class="abs" style="left:0;top:2986px;width:1180px;text-align:center;font-size:14.5px;color:var(--blue);font-weight:500">DANIEL MOORE</div>

<!-- footer -->
<footer class="abs footer"></footer>
<div class="abs logo" style="left:139px;top:3105px;color:#fff">KLARVIK</div>
<div class="abs soc" style="left:140px;top:3186px;width:32px;height:32px;border-radius:50%;background:var(--yellow)"></div>
<div class="abs soc" style="left:185px;top:3186px;width:32px;height:32px;border-radius:50%;background:var(--yellow)"></div>
<div class="abs soc" style="left:229px;top:3186px;width:32px;height:32px;border-radius:50%;background:var(--yellow)"></div>

<div class="abs f-title" style="left:369px">Quick Links</div>
<div class="abs f-rule" style="left:369px"></div>
<div class="abs f-links">Home<br>About US<br>Products<br>Services<br>Contact Us</div>

<div class="abs f-title" style="left:563px">Newsletter</div>
<div class="abs f-rule" style="left:563px"></div>
<div class="abs f-news">Stay tune with our latest<br>updates and offers.</div>
<div class="abs f-input">Email Address</div>
<div class="abs f-go"><svg width="12" height="20" viewBox="0 0 12 20"><polyline points="2,2 10,10 2,18" fill="none" stroke="#fff" stroke-width="2"/></svg></div>

<div class="abs f-title" style="left:860px">Contact Us</div>
<div class="abs f-rule" style="left:860px"></div>
<div class="abs f-ico" style="top:3157px"><svg width="12" height="14" viewBox="0 0 12 14"><path d="M6 13S1 8 1 5a5 5 0 0 1 10 0c0 3-5 8-5 8z" fill="#fff"/><circle cx="6" cy="5" r="1.8" fill="#4e86c9"/></svg></div>
<div class="abs f-contact" style="top:3155px"><b style="font-weight:600">KLARVIK,</b><br>No 48, Fjord House,<br>LINDARVIK, Iceland</div>
<div class="abs f-ico" style="top:3252px"><svg width="12" height="12" viewBox="0 0 24 24"><path d="M6.6 10.8a15 15 0 0 0 6.6 6.6l2.2-2.2a1 1 0 0 1 1-.25 11.4 11.4 0 0 0 3.6.57 1 1 0 0 1 1 1V20a1 1 0 0 1-1 1A17 17 0 0 1 3 4a1 1 0 0 1 1-1h3.5a1 1 0 0 1 1 1c0 1.25.2 2.45.57 3.57a1 1 0 0 1-.25 1z" fill="#fff"/></svg></div>
<div class="abs f-contact" style="top:3250px">+123-5550142876</div>
<div class="abs f-ico" style="top:3293px"><svg width="12" height="10" viewBox="0 0 12 10"><rect x="0.5" y="0.5" width="11" height="9" fill="#fff"/><polyline points="0.5,0.5 6,5 11.5,0.5" fill="none" stroke="#4e86c9" stroke-width="1.2"/></svg></div>
<div class="abs f-contact" style="top:3291px">info@klarvik.com</div>

<div class="abs copy">Copyrights @ 2020 KLARVIK. All Rights Reserved.</div>

</body>
</html>
```